**** Web design project for VornaSoft ****

For my ICT company VornaSoft I need a website.

We design, build and host web-applications and we have our own CMS product. In the references part we want to show sample websites (thumbnails) + links.

It should look modern (WEB 2.0), rounded corners.

I want the following menu' s:
- Home
- Services
- References
- News
- About VornaSoft
- Contact

Sample websites:
See attachments
http://www.plumvest.com
http://www.gadomirbureauwerk.nl

Reason: Want to take some time for feedback and improvements.

Reason: I'm waiting for a black background, with shadow and ambient light. You'll make a good chance!

Industry/Entity Type

It Company

Requirements
Must have
• - Fixed width (1024px), should fit on an IPad2
- Language selection English/Dutch
- Chirpline/Friendloop/Workweave/FeedPost icons
- Footer for Terms of use and Copyrights
- Search box
- 3 (or more) boxes for information i.e. news, blog or advertisements
Nice to have
• - Footer Site Map
- Contrasting background outside borders
- wide image (rotator) (with transperant sentence block)
- Shadow

```html
<!DOCTYPE html>
<html lang="en">
<head>
<meta charset="utf-8">
<title>VornaSoft</title>
<link href="https://fonts.googleapis.com/css2?family=Arimo:wght@400;700&display=swap" rel="stylesheet">
<style>
:root{
  --blue:#2f86c4;
  --blue-dark:#1f6aa6;
  --blue-light:#3aa6dc;
  --frame:#2aa0d8;
  --heading:#3d6fa6;
  --text:#666;
  --text-dark:#333;
  --panel:#ececec;
  --white:#fff;
}
*{margin:0;padding:0;box-sizing:border-box}
html,body{width:844px;height:1200px;overflow:hidden}
body{position:relative;font-family:Arimo,Arial,sans-serif;background:var(--panel);color:var(--text)}
.abs{position:absolute}

.site-header{left:0;top:0;width:844px;height:81px;background:linear-gradient(90deg,#fff 0 338px,#f1f1f1 338px)}
.brand{left:30px;top:22px;display:flex;align-items:center;gap:10px}
.brand-dot{width:38px;height:38px;border-radius:50%;background:var(--blue)}
.brand-name{font-size:24px;color:var(--blue-dark);letter-spacing:1px}
.lang{top:34px;font-size:12px;color:#888}
.lang-en{left:527px}.lang-nl{left:603px}
.header-sep{left:657px;top:16px;width:1px;height:48px;background:#c8dced}
.social-top{left:668px;top:26px;display:flex;gap:8px}
.net{display:flex;flex-direction:column;align-items:center;gap:2px;font-size:8px;color:#555}
.net i{display:block;width:24px;height:24px;border-radius:4px}
.c-chirp{background:#5fc8e6}.c-weave{background:#1f7fb8}.c-friend{background:#3c5b9a}.c-feed{background:#f08a24}

.main-nav{left:0;top:81px;width:844px;height:43px;background:linear-gradient(#3aa2dc,#2478b6);border-bottom:1px solid #1d5f92}
.main-nav ul{list-style:none;display:flex;height:100%}
.main-nav li{height:100%;display:flex;align-items:center;padding:0 19px 0 30px;color:var(--white);font-size:11px;letter-spacing:.6px;border-right:1px solid rgba(0,0,0,.15)}
.main-nav li+li{padding-left:19px}
.main-nav li:last-child{border:0}
.search{left:659px;top:93px;width:156px;height:20px;background:#fff;border-radius:2px;border:1px solid #bcd;font-size:11px;color:#888;padding:3px 8px}

.hero{left:0;top:124px;width:844px;height:352px;background:linear-gradient(#cfcfcf,#e6e6e6 55%,#bdbdbd 56%,#d8d8d8)}
.hero-title{left:25px;top:146px;font-size:32px;color:var(--heading);letter-spacing:1.5px}
.slide{border:4px solid var(--frame)}
.slide-photo{width:100%;height:100%}
.s-left{left:69px;top:227px;width:204px;height:151px}
.s-left .slide-photo{background:linear-gradient(135deg,#3a6fb0,#c9dcf2 60%,#f4f4f4)}
.s-right{left:572px;top:227px;width:205px;height:151px}
.s-right .slide-photo{background:linear-gradient(120deg,#555,#cfcfcf 50%,#f0e0d0)}
.s-center{left:271px;top:197px;width:303px;height:201px;border-width:5px;background:#fff;padding:0}
.s-center .slide-photo{background:radial-gradient(circle at 50% 45%,#3b5c8c,#10203a 45%,#f4f8fc 75%)}
.reflection{opacity:.25;background:linear-gradient(#9aa,transparent);height:60px}
.r-left{left:69px;top:380px;width:204px}.r-center{left:271px;top:400px;width:303px}.r-right{left:572px;top:380px;width:205px}
.arrow{width:41px;height:41px;border-radius:50%;background:linear-gradient(#fff,#ddd);border:1px solid #aaa;top:271px}
.arrow svg{display:block;margin:10px auto}
.arrow-prev{left:22px}.arrow-next{left:781px}

.services{left:0;top:476px;width:527px;height:559px;background:#efefef}
.services-head{left:0;top:0;width:527px;height:57px;background:linear-gradient(#fff,#efefef);border-bottom:1px solid #d4d4d4}
.services-head h2{position:absolute;left:29px;top:16px;font-size:25px;font-weight:400;color:var(--heading);letter-spacing:1.5px}
.service h3{position:absolute;font-size:15px;color:var(--text-dark);letter-spacing:.6px}
.service p{position:absolute;width:188px;font-size:10px;line-height:11.6px;text-align:justify;color:#777}
.btn{position:absolute;background:linear-gradient(#3d9fd8,#1f6ea8);color:#fff;border-radius:3px;font-size:12px;display:flex;align-items:center;justify-content:center;box-shadow:0 1px 2px rgba(0,0,0,.3)}
.shot{position:absolute;left:234px;width:244px;height:146px;border:1px solid var(--frame)}
.shot-cms{background:linear-gradient(160deg,#dfe8f2,#f4f4f4 50%,#cfcfcf)}
.shot-design{background:linear-gradient(90deg,#fafafa 60%,#8c8c8c 80%,#333)}
.divider{left:30px;top:297px;width:447px;height:1px;background:#cfcfcf}

.articles{left:527px;top:476px;width:317px;height:559px;background:linear-gradient(90deg,#dcdcdc,#f0f0f0 30%,#ececec)}
.articles-title{left:27px;top:17px;font-size:16px;color:var(--heading);letter-spacing:.5px}
.article h3{position:absolute;left:27px;font-size:17px;font-weight:400;color:#333}
.article p{position:absolute;left:28px;width:270px;font-size:7.5px;line-height:11.6px;color:#888}
.article .btn{left:25px;width:68px;height:17px;font-size:8.5px}
.icon{position:absolute;left:246px;width:24px;height:20px}

.testimonial-band{left:0;top:1035px;width:844px;height:80px;background:linear-gradient(#dde9f4,#9fc4e6)}
.social-foot{left:28px;top:1027px;display:flex;gap:16px}
.social-foot .net i{width:44px;height:44px;border-radius:3px;box-shadow:3px 3px 0 rgba(0,0,0,.15)}
.social-foot .net{font-size:9px;color:#35577a}
.quote-mark{left:293px;top:1042px;font-size:50px;font-weight:700;color:#fff;line-height:1}
.quote{left:338px;top:1053px;width:470px;font-size:19.5px;font-weight:700;color:#fff;line-height:24px}

.site-footer{left:0;top:1115px;width:844px;height:85px;background:linear-gradient(#3a9ad6,#2d7fc0)}
.footer-links{position:absolute;top:46px;left:0;width:100%;font-size:12px;font-weight:700;color:#fff}
.footer-links span{position:absolute}
.foot-brand{right:26px;top:22px;display:flex;align-items:center;gap:6px;color:#fff;font-size:13px}
.foot-brand i{display:block;width:30px;height:30px;border-radius:50%;background:rgba(255,255,255,.35)}
</style>
</head>
<body>

<header class="site-header abs">
  <div class="brand abs"><span class="brand-dot"></span><span class="brand-name">VornaSoft</span></div>
  <span class="lang lang-en abs">english</span>
  <span class="lang lang-nl abs">dutch</span>
  <div class="header-sep abs"></div>
  <div class="social-top abs">
    <span class="net"><i class="c-chirp"></i>Chirpline</span>
    <span class="net"><i class="c-weave"></i>Workweave</span>
    <span class="net"><i class="c-friend"></i>Friendloop</span>
    <span class="net"><i class="c-feed"></i>FeedPost</span>
  </div>
</header>

<nav class="main-nav abs">
  <ul><li>HOME</li><li>SERVICES</li><li>ABOUT</li><li>NEWS</li><li>CONTACT</li><li>REFERENCES</li></ul>
</nav>
<div class="search abs">search</div>

<section class="hero abs"></section>
<h1 class="hero-title abs" style="font-weight:400">Welcome to VornaSoft</h1>
<div class="slide s-left abs"><div class="slide-photo" role="img" aria-label="Photo of a woman with a laptop in front of a glass building"></div></div>
<div class="slide s-right abs"><div class="slide-photo" role="img" aria-label="Photo of a hand typing on a laptop keyboard"></div></div>
<div class="slide s-center abs"><div class="slide-photo" role="img" aria-label="Illustration of a tablet with media tiles bursting out of the screen"></div></div>
<div class="reflection r-left abs"></div>
<div class="reflection r-center abs"></div>
<div class="reflection r-right abs"></div>
<div class="arrow arrow-prev abs"><svg width="14" height="20"><path d="M11 2 3 10l8 8" fill="none" stroke="#777" stroke-width="3"/></svg></div>
<div class="arrow arrow-next abs"><svg width="14" height="20"><path d="M3 2l8 8-8 8" fill="none" stroke="#777" stroke-width="3"/></svg></div>

<section class="services abs">
  <div class="services-head abs"><h2>What we do</h2></div>
  <div class="service">
    <h3 style="left:30px;top:94px">CMS Product</h3>
    <p style="left:30px;top:121px">Lorem ipsum dolor sit amet, consectetuer adipiscing elit, sed diam nonummy nibh euismod tincidunt ut laoreet dolore magna aliquam erat volutpat. Ut wisi enim ad minim veniam, quis nostrud exerci tation ullamcorper suscipit lobortis nisl ut aliquip ex ea com</p>
    <span class="btn" style="left:29px;top:213px;width:85px;height:23px">take the tour</span>
    <div class="shot shot-cms" style="top:122px" role="img" aria-label="Screenshot of a CMS editor with figures arranged on a canvas"></div>
  </div>
  <div class="divider abs"></div>
  <div class="service">
    <h3 style="left:30px;top:334px">Web Application Design</h3>
    <p style="left:30px;top:362px">Lorem ipsum dolor sit amet, consectetuer adipiscing elit, sed diam nonummy nibh euismod tincidunt ut laoreet dolore magna aliquam erat volutpat. Ut wisi enim ad minim veniam, quis nostrud exerci tation ullamcorper suscipit lobortis nisl ut aliquip ex ea com</p>
    <span class="btn" style="left:28px;top:456px;width:83px;height:25px">take the tour</span>
    <div class="shot shot-design" style="top:361px" role="img" aria-label="Photo of a hand drawing a design mind map on glass"></div>
  </div>
</section>

<aside class="articles abs">
  <h2 class="articles-title abs" style="font-weight:700">Recent Articles</h2>
  <div class="article">
    <h3 style="top:51px">latest news</h3>
    <svg class="icon" style="top:46px" viewBox="0 0 24 20"><rect x="1" y="1" width="22" height="18" rx="1" fill="#f4f4f4" stroke="#888"/><path d="M4 6h16M4 10h16M4 14h10" stroke="#999"/></svg>
    <p style="top:81px">Lorem ipsum dolor sit amet, consectetuer adipiscing elit, sed diam nonummy nibh euismod tincidunt ut laoreet dolore magna aliquam erat volutpat. Ut wisi enim ad minim veniam, quis nostrud exerci tation ullamcorper suscipit lobortis nisl ut aliquip ex ea com</p>
    <span class="btn" style="top:141px">read more</span>
  </div>
  <div class="article">
    <h3 style="top:187px">technology update</h3>
    <svg class="icon" style="top:180px" viewBox="0 0 24 20"><rect x="1" y="1" width="22" height="14" fill="#4aa6e8" stroke="#777"/><rect x="9" y="15" width="6" height="3" fill="#888"/></svg>
    <p style="top:217px">Lorem ipsum dolor sit amet, consectetuer adipiscing elit, sed diam nonummy nibh euismod tincidunt ut laoreet dolore magna aliquam erat volutpat. Ut wisi enim ad minim veniam, quis nostrud exerci tation ullamcorper suscipit lobortis nisl ut aliquip ex ea com</p>
    <span class="btn" style="top:276px">read more</span>
  </div>
  <div class="article">
    <h3 style="top:317px">visit our blog</h3>
    <svg class="icon" style="top:313px" viewBox="0 0 24 20"><path d="M1 2h20v11H8l-4 4v-4H1z" fill="#fff" stroke="#888"/><path d="M19 9v8M15 13h8" stroke="#6cbf2e" stroke-width="3"/></svg>
    <p style="top:345px">Lorem ipsum dolor sit amet, consectetuer adipiscing elit, sed diam nonummy nibh euismod tincidunt ut laoreet dolore magna aliquam erat volutpat. Ut wisi enim ad minim veniam, quis nostrud exerci tation ullamcorper suscipit lobortis nisl ut aliquip ex ea com</p>
    <span class="btn" style="top:406px">read more</span>
  </div>
  <div class="article">
    <h3 style="top:443px">our partners</h3>
    <svg class="icon" style="top:438px" viewBox="0 0 24 20"><circle cx="8" cy="6" r="4" fill="#333"/><circle cx="16" cy="6" r="4" fill="#555"/><path d="M1 19c0-6 14-6 14 0zM10 19c0-6 13-6 13 0z" fill="#444"/></svg>
    <p style="top:471px">Lorem ipsum dolor sit amet, consectetuer adipiscing elit, sed diam nonummy nibh euismod tincidunt ut laoreet dolore magna aliquam erat volutpat. Ut wisi enim ad minim veniam, quis nostrud exerci tation ullamcorper suscipit lobortis nisl ut aliquip ex ea com</p>
    <span class="btn" style="top:530px">read more</span>
  </div>
</aside>

<section class="testimonial-band abs"></section>
<div class="social-foot abs">
  <span class="net"><i class="c-chirp"></i>Chirpline</span>
  <span class="net"><i class="c-weave"></i>Workweave</span>
  <span class="net"><i class="c-friend"></i>Friendloop</span>
  <span class="net"><i class="c-feed"></i>FeedPost</span>
</div>
<span class="quote-mark abs">&ldquo;</span>
<p class="quote abs">Testimonial for what clients say about you or a social media quote.</p>

<footer class="site-footer abs">
  <div class="footer-links">
    <span style="left:226px">Contact Us</span>
    <span style="left:315px">Privacy Policy</span>
    <span style="left:434px">Site Map</span>
    <span style="left:524px">Help</span>
    <span style="left:583px">FAQ's</span>
  </div>
  <div class="foot-brand abs"><i></i>VornaSoft</div>
</footer>

</body>
</html>
```